Over 100 ladies will be traveling to Ocean City, MD for a Women's Retreat Conference. This flyer is for advertisement. This flyer is to circulate for registrations as well as to post on social media. Theme is Holy Spirit fire. I have attached a photo. All the information in the attachment should be included on the flyer. Information should be clearly readable end eye catching.

Target Market(s)

Church ladies

Industry/Entity Type

Religious

Font styles to use
Sans Serif

Colors

Designer to choose colors to be used in the design.

Requirements
Must have
• Title: Brightvale Womens Gathering 2019 "FIRE"
• All components in attachments

```html
<!DOCTYPE html>
<html lang="en">
<head>
<meta charset="utf-8">
<title>Brightvale Women's Gathering 2019 — FIRE</title>
<link href="https://fonts.googleapis.com/css2?family=Oswald:wght@300;500;600;700&family=Montserrat:wght@400;500;700;800&display=swap" rel="stylesheet">
<style>
  :root {
    --ink: #0d0d0d;
    --white: #ffffff;
    --red: #e00d0d;
    --red-deep: #b30606;
    --flame-hot: #ffe36a;
    --flame-mid: #ff9a1a;
    --flame-low: #c8200a;
    --gold: #ffd21f;
    --grey: #2a2a2a;
  }
  * { margin: 0; padding: 0; box-sizing: border-box; }
  html, body { width: 848px; height: 1200px; overflow: hidden; background: var(--ink); }
  .flyer {
    position: relative; width: 848px; height: 1200px; overflow: hidden;
    font-family: "Montserrat", sans-serif; color: var(--white);
    background:
      radial-gradient(ellipse 70% 35% at 50% 30%, rgba(120,30,10,0.35), transparent 70%),
      radial-gradient(ellipse 60% 20% at 50% 95%, rgba(90,90,90,0.35), transparent 70%),
      linear-gradient(180deg, #1a1a1a 0%, #111 45%, #0b0b0b 100%);
  }
  .abs { position: absolute; }
  .center { left: 0; width: 100%; text-align: center; }

  .kicker { top: 30px; font-family: "Oswald", sans-serif; font-weight: 300; font-size: 54px; line-height: 1; color: var(--red); letter-spacing: 1px; }
  .title { top: 90px; font-family: "Oswald", sans-serif; font-weight: 600; font-size: 96px; line-height: 1; letter-spacing: -1px; }
  .theme {
    top: 190px; font-family: "Oswald", sans-serif; font-weight: 700; font-size: 250px; line-height: 1.05; letter-spacing: 6px;
    background: linear-gradient(180deg, var(--flame-hot) 0%, var(--flame-mid) 40%, var(--flame-low) 100%);
    -webkit-background-clip: text; background-clip: text; color: transparent;
    filter: drop-shadow(0 0 18px rgba(255,120,20,0.55));
  }

  .dates { top: 504px; font-weight: 800; font-size: 40px; line-height: 1; }
  .venue { top: 570px; font-weight: 800; font-size: 30px; line-height: 1; color: var(--red); }
  .address { top: 612px; font-weight: 400; font-size: 26px; line-height: 1; }

  .side-block { background: linear-gradient(180deg, #333, #222); opacity: 0.8; }
  .side-left { left: 0; top: 676px; width: 64px; height: 140px; }
  .side-right { left: 772px; top: 788px; width: 76px; height: 128px; }

  .include-label { left: 92px; top: 672px; font-weight: 500; font-size: 22px; color: var(--red); }
  .perks { list-style: none; }
  .perks li { display: flex; align-items: center; gap: 14px; font-size: 21px; height: 32px; }
  .perks svg { width: 17px; height: 17px; flex: none; }
  .perks-left { left: 92px; top: 700px; }
  .perks-right { left: 490px; top: 694px; }

  .price { left: 338px; top: 783px; width: 98px; height: 34px; }
  .price-tag { position: absolute; inset: 0; }
  .price-amount { position: absolute; inset: 0; display: flex; align-items: center; justify-content: center; font-weight: 700; font-size: 22px; }
  .price-amount sup { font-size: 11px; margin-right: 1px; }
  .price-note { left: 448px; top: 793px; font-size: 12px; }

  .speaker { top: 860px; width: 272px; text-align: center; }
  .speaker .portrait { width: 112px; height: 112px; margin: 0 auto; border-radius: 50%; border: 4px solid #e8e8e8; background: radial-gradient(circle at 50% 40%, #8a5a3c, #3b2418 75%); }
  .speaker .name { margin-top: 22px; font-weight: 800; font-size: 16px; color: var(--red); }
  .speaker .role { font-size: 13px; line-height: 18px; }
  .speaker .role.em { font-style: italic; }
  .speaker-1 { left: 10px; }
  .speaker-2 { left: 282px; }
  .speaker-3 { left: 555px; }
  .divider { top: 876px; width: 1px; height: 140px; background: var(--red-deep); }

  .terms {
    left: 28px; top: 1062px; width: 792px; height: 80px;
    border: 1.5px solid var(--red); border-bottom: none; border-radius: 18px 18px 0 0;
    padding: 10px 20px 0; text-align: center; font-size: 12px; line-height: 17px;
  }
  .contact-band {
    left: 0; top: 1136px; width: 848px; height: 64px; background: var(--red);
    display: flex; flex-direction: column; justify-content: center; text-align: center;
    font-size: 18px; line-height: 23px; font-weight: 500;
  }
  .contact-band strong { color: var(--gold); font-weight: 700; }
</style>
</head>
<body>
<main class="flyer">
  <h2 class="abs center kicker">BRIGHTVALE WOMEN'S</h2>
  <h1 class="abs center title">GATHERING 2019</h1>
  <p class="abs center theme">FIRE</p>

  <p class="abs center dates">NOVEMBER 7-9</p>
  <p class="abs center venue">HARBORLINE MANOR HOTEL &amp; SUITES</p>
  <p class="abs center address">1450 Seabreeze Ave., Ocean City, Maryland 21842</p>

  <div class="abs side-block side-left" role="img" aria-label="Striped chevron accent"></div>
  <div class="abs side-block side-right" role="img" aria-label="Striped chevron accent"></div>

  <p class="abs include-label">Include</p>
  <ul class="abs perks perks-left">
    <li><svg viewBox="0 0 20 20"><rect x="1.5" y="3.5" width="14" height="14" rx="2" fill="none" stroke="#e00d0d" stroke-width="2"/><path d="M5 10l3.5 3.5L18 3" fill="none" stroke="#e00d0d" stroke-width="2.4" stroke-linecap="round"/></svg>All Retreat Sessions</li>
    <li><svg viewBox="0 0 20 20"><rect x="1.5" y="3.5" width="14" height="14" rx="2" fill="none" stroke="#e00d0d" stroke-width="2"/><path d="M5 10l3.5 3.5L18 3" fill="none" stroke="#e00d0d" stroke-width="2.4" stroke-linecap="round"/></svg>2 Nights Hotel Accommodations</li>
  </ul>
  <ul class="abs perks perks-right">
    <li><svg viewBox="0 0 20 20"><rect x="1.5" y="3.5" width="14" height="14" rx="2" fill="none" stroke="#e00d0d" stroke-width="2"/><path d="M5 10l3.5 3.5L18 3" fill="none" stroke="#e00d0d" stroke-width="2.4" stroke-linecap="round"/></svg>1 Hot Lunch Buffet</li>
    <li><svg viewBox="0 0 20 20"><rect x="1.5" y="3.5" width="14" height="14" rx="2" fill="none" stroke="#e00d0d" stroke-width="2"/><path d="M5 10l3.5 3.5L18 3" fill="none" stroke="#e00d0d" stroke-width="2.4" stroke-linecap="round"/></svg>1 Full Hot American Breakfast</li>
  </ul>

  <div class="abs price">
    <svg class="price-tag" viewBox="0 0 98 34" preserveAspectRatio="none"><defs><linearGradient id="tagFill" x1="0" x2="1"><stop offset="0" stop-color="#b30606"/><stop offset="1" stop-color="#e51a1a"/></linearGradient></defs><polygon points="8,0 98,0 90,34 0,34" fill="url(#tagFill)"/></svg>
    <span class="price-amount"><sup>$</sup>295</span>
  </div>
  <p class="abs price-note">*Based on double occupancy</p>

  <div class="abs speaker speaker-1">
    <div class="portrait" role="img" aria-label="Portrait photo of Apostle Delia Renfield"></div>
    <p class="name">APOSTLE DELIA RENFIELD</p>
    <p class="role em">Retreat Host</p>
    <p class="role em">Retreat Speaker</p>
  </div>
  <div class="abs divider" style="left:290px"></div>
  <div class="abs speaker speaker-2">
    <div class="portrait" role="img" aria-label="Portrait photo of Pastor Marisa Cole"></div>
    <p class="name">PASTOR MARISA COLE</p>
    <p class="role">Orlando, Florida</p>
    <p class="role em">Retreat Speaker</p>
  </div>
  <div class="abs divider" style="left:550px"></div>
  <div class="abs speaker speaker-3">
    <div class="portrait" role="img" aria-label="Portrait photo of Pastor Lenora Whitby"></div>
    <p class="name">PASTOR LENORA WHITBY</p>
    <p class="role">NLCC - Waldorf, Maryland</p>
    <p class="role em">Retreat Speaker</p>
  </div>

  <p class="abs terms">**ALL deposits/registrations are NON-refundable and NON-transferable. Your entire registration is due by October 1, 2019. Please submit your desired roommate's name at the time of registration. If you do not choose a roommate one will be assigned to you unless you have registered for a private room.</p>

  <footer class="abs contact-band">
    <p>For more information visit us <strong>brightvale2019.tixhub.com</strong> or contact Ariel via email</p>
    <p><strong>ariel@deliarenfieldministries.com</strong> or phone <strong>240-555-0147</strong></p>
  </footer>
</main>
</body>
</html>
```